Vantor Medica Innovative Business Card

Stunning business card. Background will be black. Letters in gold. Modern yet simple design that is attention grabbing. QR code leading to site. Attractive primarily to males ages 30 to 50 but also to females in same age range looking for beauty and mental health products

Target Market(s)

Males in the 30-50 age demographics

Industry/Entity Type

Pharmaceuticals selling erectile dysfunction and mens health medications

Contact Information for Business Card

www.vantormedica.example; (775) BUY-KELO; info@vantormedica.example

Colors
FFC000
F8CF3A
FAE287
FDF2CF
FEFAEE

Requirements
Must have
• Black business card with gold letters.
Nice to have
• perhaps just the logo or the "R" icon by itself on one side
Should not have
• too much content so it does not look busy

```html
<!DOCTYPE html>
<html lang="en">
<head>
<meta charset="utf-8">
<title>Vantor Medica Business Card</title>
<link href="https://fonts.googleapis.com/css2?family=Montserrat:wght@400;800&display=swap" rel="stylesheet">
<style>
  :root {
    --canvas: #dddcdd;
    --card: #000000;
    --gold: #e2bf48;
    --gold-dark: #9c7622;
    --gold-light: #f3d45c;
    --gold-mid: #c99f35;
  }
  html, body {
    margin: 0;
    padding: 0;
    width: 1199px;
    height: 1200px;
    overflow: hidden;
    background: var(--canvas);
  }
  .canvas {
    position: relative;
    width: 1199px;
    height: 1200px;
    background: var(--canvas);
  }
  .card {
    position: absolute;
    left: 162px;
    width: 873px;
    height: 510px;
    background: var(--card);
    overflow: hidden;
    box-shadow: 0 2px 6px rgba(0,0,0,0.35);
  }
  .card--front { top: 75px; }
  .card--back { top: 624px; }

  .pattern-area {
    position: absolute;
    background: linear-gradient(135deg, rgba(201,159,53,0.55) 0%, rgba(156,118,34,0.25) 55%, rgba(0,0,0,0) 100%);
  }
  .card--front .pattern-area--top {
    left: 479px; top: 0; width: 394px; height: 288px;
    background: linear-gradient(225deg, rgba(226,191,72,0.6) 0%, rgba(156,118,34,0.25) 55%, rgba(0,0,0,0) 100%);
  }
  .card--front .pattern-area--bottom {
    left: 31px; top: 398px; width: 338px; height: 112px;
    background: linear-gradient(45deg, rgba(226,191,72,0.55) 0%, rgba(156,118,34,0.2) 60%, rgba(0,0,0,0) 100%);
  }
  .card--back .pattern-area--main {
    left: 0; top: 17px; width: 615px; height: 391px;
    background: linear-gradient(135deg, rgba(226,191,72,0.55) 0%, rgba(156,118,34,0.25) 55%, rgba(0,0,0,0) 100%);
  }

  .brand {
    position: absolute;
    display: flex;
    flex-direction: column;
    align-items: center;
    color: var(--gold);
    font-family: "Montserrat", sans-serif;
    font-weight: 800;
  }
  .brand__mark {
    width: 56px;
    height: 56px;
    border-radius: 50%;
    background: var(--gold);
    margin-bottom: 20px;
  }
  .brand__name {
    font-size: 38px;
    line-height: 1.05;
    letter-spacing: 4px;
    text-transform: uppercase;
    text-align: center;
  }
  .card--front .brand { left: 75px; top: 108px; width: 300px; }
  .card--back .brand { left: 477px; top: 200px; width: 320px; }

  .contact {
    position: absolute;
    left: 510px;
    top: 336px;
    margin: 0;
    padding: 0;
    list-style: none;
    font-family: "Montserrat", sans-serif;
    font-weight: 400;
    font-size: 20px;
    color: var(--gold);
  }
  .contact__item {
    display: flex;
    align-items: center;
    height: 40px;
    white-space: nowrap;
  }
  .contact__icon {
    width: 16px;
    height: 16px;
    margin-right: 10px;
    fill: var(--gold);
    flex: none;
  }
</style>
</head>
<body>
<div class="canvas">

  <section class="card card--front">
    <div class="pattern-area pattern-area--top" role="img" aria-label="Gold diagonal stripe pattern"></div>
    <div class="pattern-area pattern-area--bottom" role="img" aria-label="Gold diagonal stripe pattern"></div>
    <div class="brand">
      <div class="brand__mark"></div>
      <div class="brand__name">Vantor<br>Medica</div>
    </div>
    <ul class="contact">
      <li class="contact__item">
        <svg class="contact__icon" viewBox="0 0 16 16"><path d="M3.5 1.5l2.5 0 1 3.5-1.6 1.2a8 8 0 0 0 4.4 4.4L11 9l3.5 1v2.5c0 1-1 2-2 2C6.5 14.5 1.5 9.5 1.5 3.5c0-1 1-2 2-2z"/></svg>
        (775) BUY-KELO
      </li>
      <li class="contact__item">
        <svg class="contact__icon" viewBox="0 0 16 16"><circle cx="8" cy="8" r="6.5" fill="none" stroke="#e2bf48" stroke-width="1.6"/><path d="M1.5 8h13M8 1.5c-3 3.5-3 9.5 0 13M8 1.5c3 3.5 3 9.5 0 13" fill="none" stroke="#e2bf48" stroke-width="1.4"/></svg>
        www.vantormedica.example
      </li>
      <li class="contact__item">
        <svg class="contact__icon" viewBox="0 0 16 16"><rect x="1" y="3" width="14" height="10" rx="1"/><path d="M1.5 3.5L8 9l6.5-5.5" fill="none" stroke="#000" stroke-width="1.3"/></svg>
        info@vantormedica.example
      </li>
    </ul>
  </section>

  <section class="card card--back">
    <div class="pattern-area pattern-area--main" role="img" aria-label="Gold diagonal stripe pattern"></div>
    <div class="brand">
      <div class="brand__mark"></div>
      <div class="brand__name">Vantor<br>Medica</div>
    </div>
  </section>
</div>
</body>
</html>
```